Products & Services Postcard For our Vacuum Repair Store & Carpet Cleaning Company

SEE ATTACHED DOCUMENTS FOR FRONT AND BACK OF CARD.
Also, Brand logos are available in my attachments

We are a Retail Vacuum Repair shop and we also have Three carpet cleaning trucks that operate out of our location. In addition to servicing Vacuum Cleaners we also offer in home cleaning services that include: Carpet cleaning, upholstery cleaning, tile & Grout Cleaning, general cleaning services, move out clean ups, one time cleanings, post construction cleanup and strip & wax floorsWe Need to design a KRTB(pvlo quiet lane parcel) postcard that shows and tells everything we do. Postcard should include all our services, have before and after pictures, list benefits of doing business with us and should have coupons attached to create urgency to call usWe:Fully Insured, commercial & Residential, free estimatesWe are the only Vacuum Store in area that is a Certified SVAPN Cleaner.Also, the only SVAPN Certified cleaner that services Vacuum Cleaners.We have a great reputation as a 5 Star Vacuum Service Station and Also a 5 Star Cleaning Company. We are a one stop shop for ALL your cleaning needs.Our goal is to educate customers and provide options.Goal of the card is to get customers to call or stop in for advice on both their vacuum cleaner and cleaning their homes. Goal is to get phone to ring or get people through the door.

Target Market(s)

Homeowners, People interested in clean

Colors

Designer to choose colors to be used in the design.

Requirements
Must have
• Before & After pics
• Coupons
• List of services
• Call to Action
• Address
• Phone #
Nice to have
• One side of postcard could be about our Vacuum Cleaner repair shop.
• The other side could be about our cleaning business

```html
<!DOCTYPE html>
<html lang="en">
<head>
<meta charset="utf-8">
<title>Meridian Vacuums – KRTB Postcard</title>
<link href="https://fonts.googleapis.com/css2?family=Bebas+Neue&family=Oxygen:wght@300;400;700&family=Montserrat:wght@500;600;700&family=Roboto+Condensed:wght@400;700&display=swap" rel="stylesheet">
<style>
:root{
  --teal:#18433e;
  --sage:#b4c07d;
  --ink:#111;
  --white:#fff;
  --coupon-ink:#6b2b18;
  --price:#6f9236;
  --cta-yellow:#d6dc7c;
  --bg:#dcdcdc;
}
*{margin:0;padding:0;box-sizing:border-box}
html,body{width:991px;height:1200px;overflow:hidden;background:var(--bg)}
.canvas{position:relative;width:991px;height:1200px}
.card{position:absolute;left:116px;width:772px;height:498px;overflow:hidden}
.card--front{top:74px;background:linear-gradient(180deg,var(--teal) 0 60%,#557f77 82%,#6c928a 100%)}
.card--back{top:614px;background:var(--white)}
.abs{position:absolute;white-space:nowrap}
.display{font-family:"Bebas Neue",sans-serif;font-weight:400;line-height:1}
.body{font-family:"Oxygen",sans-serif}
.round{font-family:"Montserrat",sans-serif}
.condensed{font-family:"Roboto Condensed",sans-serif}

/* front */
.front-panel{left:25px;top:24px;width:410px;height:340px;background:var(--white);clip-path:polygon(0 0,85px 0,110px 26px,100% 26px,100% 100%,0 100%)}
.front-divider{left:322px;top:50px;width:6px;height:314px;background:#e8ece0}
.tagline{left:142px;top:16px;font-size:29px;color:var(--white)}
.tagline span{color:var(--sage)}
.headline{left:52px;top:66px;color:var(--ink)}
.headline .l1{font-size:37px;display:block}
.headline .l2{font-size:48px;display:block;margin-top:2px}
.sub-band{left:16px;top:152px;width:284px;height:28px;background:var(--sage);color:var(--white);font-size:17px;font-weight:500;padding:3px 0 0 30px}
.service-list{left:52px;top:188px;list-style:none;font-size:12px;color:#222}
.service-list li{height:16.4px;display:flex;align-items:center;gap:4px}
.tick{width:10px;height:10px;flex:none}
.quality-badge{left:229px;top:243px;width:75px;height:75px}
.motto{left:52px;top:330px;font-size:13px;font-weight:700;color:#222}
.brand-tile{left:331px;top:65px;width:108px;height:88px;background:linear-gradient(160deg,#8fb3ad,#4e7c75)}
.brand-name{position:absolute;left:0;right:0;bottom:14px;text-align:center;font-family:"Oxygen",sans-serif;font-weight:700;font-size:12.5px;color:var(--white);line-height:1.15}
.photo--before{left:331px;top:162px;width:108px;height:88px;background:linear-gradient(160deg,#b4a891,#8a7e6a)}
.photo--after{left:331px;top:261px;width:108px;height:88px;background:linear-gradient(160deg,#a49781,#6f6454)}
.photo-label{position:absolute;top:2px;left:0;right:0;text-align:center;font-family:"Montserrat",sans-serif;font-weight:700;font-size:17px;color:var(--white)}
.photo--hero{left:448px;top:50px;width:300px;height:224px;background:linear-gradient(135deg,#c9bfae 0%,#9b917f 55%,#5a5247 100%)}
.cta-box{left:386px;top:274px;width:362px;height:90px;background:#141414;clip-path:polygon(56px 0,100% 0,100% 100%,0 100%,0 62px,56px 62px)}
.cta-line{left:463px;top:291px;font-size:12.5px;color:var(--cta-yellow)}
.cta-phone{left:461px;top:304px;font-size:46px;line-height:1;font-weight:700;color:var(--white)}
.coupon{top:386px;width:140px;height:112px;padding:8px 7px}
.coupon--sage{background:var(--sage)}
.coupon--teal{background:var(--teal)}
.coupon-inner{width:100%;height:100%;background:var(--white);border:2px dashed #333;border-radius:3px;display:flex;flex-direction:column;align-items:center;justify-content:center;text-align:center;font-family:"Montserrat",sans-serif;color:var(--coupon-ink);font-size:10px;font-weight:500;line-height:1.2;white-space:normal}
.coupon-price{font-size:32px;font-weight:600;color:var(--price);line-height:1.05}
.coupon-value{font-size:14px;font-weight:500;color:var(--price)}

/* back */
.back-panel{left:0;top:0;width:514px;height:498px;background:var(--teal);clip-path:polygon(0 0,100% 0,100% 430px,338px 430px,338px 100%,0 100%)}
.back-kicker{left:48px;top:26px;font-size:44px;color:var(--white)}
.back-band{left:12px;top:70px;width:494px;height:72px;background:var(--sage)}
.back-band-fold{left:12px;top:142px;width:0;height:0;border-top:10px solid #0e2b27;border-left:12px solid transparent}
.back-title{left:48px;top:76px;font-size:78px;color:var(--white)}
.tuneup{left:48px;top:156px;font-size:19.5px;font-weight:700;color:var(--white)}
.fineprint{left:48px;top:185px;font-size:12px;font-weight:300;color:#e3e8e4;line-height:16px}
.shop-title{left:48px;top:224px;font-size:15px;color:var(--sage);font-weight:700}
.repair-list{left:48px;top:250px;list-style:none;font-size:12.5px;color:var(--white);line-height:16.4px}
.repair-list li{display:flex;gap:8px}
.repair-list li .tick{margin-top:3px}
.repair-list .lead{font-weight:700}
.repair-list .cont{padding-left:18px}
.address{left:48px;top:406px;font-size:14px;font-weight:700;color:var(--sage);line-height:19.5px}
.back-phone{left:48px;top:440px;font-size:48px;line-height:1;font-weight:700;color:var(--white)}
.photo--tile{left:338px;top:158px;width:168px;height:131px;border:5px solid #e9ece6;background:linear-gradient(135deg,#cfc6b2,#8f8572 60%,#6b6455)}
.photo--wand{left:338px;top:297px;width:168px;height:133px;border:5px solid #e9ece6;background:linear-gradient(135deg,#b9b09e,#8e8472 60%,#4f4a42)}
.postage{left:647px;top:12px;width:113px;height:110px;border:1.5px solid #222;display:flex;align-items:center;justify-content:center;text-align:center;font-family:Arial,sans-serif;font-size:14px;color:#111;line-height:18px}
.mail-block{left:530px;top:306px;width:228px;height:123px;border:1.5px solid #222;font-family:Arial,sans-serif;color:#111}
.indicia{position:absolute;right:10px;top:8px;text-align:right;font-size:7px;line-height:8.5px}
.route{position:absolute;left:38px;top:46px;font-size:9.5px}
.recipient{position:absolute;left:12px;top:84px;font-size:8.5px;font-weight:700;line-height:11px}
.barcode-label{left:502px;top:464px;font-family:Arial,sans-serif;font-size:14px;color:#111}
</style>
</head>
<body>
<main class="canvas">

  <section class="card card--front" aria-label="Postcard front">
    <div class="abs front-panel"></div>
    <div class="abs front-divider"></div>
    <div class="abs photo--hero" role="img" aria-label="Photo of an upholstery cleaning wand on fabric"></div>
    <div class="abs cta-box"></div>

    <p class="abs display tagline">Friendly, Professional, <span>SVAPN Trained Technicians</span></p>

    <h1 class="abs display headline"><span class="l1">Carpets &amp; Flooring</span><span class="l2">Need Cleaning?</span></h1>
    <p class="abs round sub-band">Furniture Need Cleaning?</p>

    <ul class="abs body service-list">
      <li><svg class="tick" viewBox="0 0 10 10"><circle cx="5" cy="5" r="4.2" fill="none" stroke="#222" stroke-width="1"/><path d="M3 5.2l1.4 1.4L7.2 3.7" fill="none" stroke="#222" stroke-width="1"/></svg>Commercial</li>
      <li><svg class="tick" viewBox="0 0 10 10"><circle cx="5" cy="5" r="4.2" fill="none" stroke="#222" stroke-width="1"/><path d="M3 5.2l1.4 1.4L7.2 3.7" fill="none" stroke="#222" stroke-width="1"/></svg>Residential</li>
      <li><svg class="tick" viewBox="0 0 10 10"><circle cx="5" cy="5" r="4.2" fill="none" stroke="#222" stroke-width="1"/><path d="M3 5.2l1.4 1.4L7.2 3.7" fill="none" stroke="#222" stroke-width="1"/></svg>General Cleaning</li>
      <li><svg class="tick" viewBox="0 0 10 10"><circle cx="5" cy="5" r="4.2" fill="none" stroke="#222" stroke-width="1"/><path d="M3 5.2l1.4 1.4L7.2 3.7" fill="none" stroke="#222" stroke-width="1"/></svg>Move In &amp; Move Out Cleanings</li>
      <li><svg class="tick" viewBox="0 0 10 10"><circle cx="5" cy="5" r="4.2" fill="none" stroke="#222" stroke-width="1"/><path d="M3 5.2l1.4 1.4L7.2 3.7" fill="none" stroke="#222" stroke-width="1"/></svg>Carpet Cleaning</li>
      <li><svg class="tick" viewBox="0 0 10 10"><circle cx="5" cy="5" r="4.2" fill="none" stroke="#222" stroke-width="1"/><path d="M3 5.2l1.4 1.4L7.2 3.7" fill="none" stroke="#222" stroke-width="1"/></svg>Tile &amp; Grout Cleaning</li>
      <li><svg class="tick" viewBox="0 0 10 10"><circle cx="5" cy="5" r="4.2" fill="none" stroke="#222" stroke-width="1"/><path d="M3 5.2l1.4 1.4L7.2 3.7" fill="none" stroke="#222" stroke-width="1"/></svg>VCT Strip &amp; Wax</li>
      <li><svg class="tick" viewBox="0 0 10 10"><circle cx="5" cy="5" r="4.2" fill="none" stroke="#222" stroke-width="1"/><path d="M3 5.2l1.4 1.4L7.2 3.7" fill="none" stroke="#222" stroke-width="1"/></svg>Furniture Cleaning</li>
    </ul>

    <svg class="abs quality-badge" viewBox="0 0 75 75" aria-hidden="true"><circle cx="37.5" cy="37.5" r="37" fill="#c4242b"/></svg>

    <p class="abs body motto">“Nobody Does It Better &amp; Gives You More”</p>

    <div class="abs brand-tile"><p class="brand-name">MERIDIAN<br>VACUUMS</p></div>
    <div class="abs photo--before" role="img" aria-label="Before photo of a soiled carpet"><span class="photo-label">Before</span></div>
    <div class="abs photo--after" role="img" aria-label="After photo of a freshly cleaned carpet"><span class="photo-label">After</span></div>

    <p class="abs condensed cta-line">Call us for a FREE Estimates on ALL Your Cleaning Needs!</p>
    <p class="abs condensed cta-phone">555-014-2290</p>

    <div class="abs coupon coupon--sage" style="left:26px"><div class="coupon-inner">Whole House<br>Carpet Cleaning Up<br>To 700 Sq Ft ONLY<span class="coupon-price">$189</span></div></div>
    <div class="abs coupon coupon--teal" style="left:170px"><div class="coupon-inner">Furniture Cleaning<span class="coupon-price">$199</span>(Sofa, Loveseat &amp;<br>Chair)</div></div>
    <div class="abs coupon coupon--sage" style="left:314px"><div class="coupon-inner">Tile &amp; Grout Cleaning<br>Kitchen Floor Only<span class="coupon-price">$119</span>(Up To 120 Sq Ft)</div></div>
    <div class="abs coupon coupon--teal" style="left:461px"><div class="coupon-inner">FREE Cleaning Kit<span class="coupon-value">(Value of $59)</span>for Your Carpet<br>When You Add<br>Protector</div></div>
    <div class="abs coupon coupon--sage" style="left:606px"><div class="coupon-inner">FREE Tile &amp; Grout<br>Cleaning Kit<span class="coupon-value">(Value of $59)</span>When you Add<br>Sealer</div></div>
  </section>

  <section class="card card--back" aria-label="Postcard back">
    <div class="abs back-panel"></div>
    <p class="abs display back-kicker">Are You Frustrated With Your</p>
    <div class="abs back-band"></div>
    <div class="abs back-band-fold"></div>
    <h2 class="abs display back-title">Vacuum Cleaner?</h2>

    <p class="abs body tuneup">Vacuum Tune Up Only $19.99</p>
    <p class="abs body fineprint">*Offer Expires in 30 days<br>**Limit One Vacuum Per Coupon</p>
    <p class="abs condensed shop-title">FIVE STAR VACUUM CLEANER REPAIR SHOP</p>

    <ul class="abs body repair-list">
      <li class="lead"><svg class="tick" viewBox="0 0 10 10"><circle cx="5" cy="5" r="4.2" fill="none" stroke="#fff" stroke-width="1"/><path d="M3 5.2l1.4 1.4L7.2 3.7" fill="none" stroke="#fff" stroke-width="1"/></svg>Our Repair Center Offers:</li>
      <li><svg class="tick" viewBox="0 0 10 10"><circle cx="5" cy="5" r="4.2" fill="none" stroke="#fff" stroke-width="1"/><path d="M3 5.2l1.4 1.4L7.2 3.7" fill="none" stroke="#fff" stroke-width="1"/></svg>Free Estimates</li>
      <li><svg class="tick" viewBox="0 0 10 10"><circle cx="5" cy="5" r="4.2" fill="none" stroke="#fff" stroke-width="1"/><path d="M3 5.2l1.4 1.4L7.2 3.7" fill="none" stroke="#fff" stroke-width="1"/></svg>Experienced &amp; Trained Technicians</li>
      <li><svg class="tick" viewBox="0 0 10 10"><circle cx="5" cy="5" r="4.2" fill="none" stroke="#fff" stroke-width="1"/><path d="M3 5.2l1.4 1.4L7.2 3.7" fill="none" stroke="#fff" stroke-width="1"/></svg>Fast, reliable service</li>
      <li><svg class="tick" viewBox="0 0 10 10"><circle cx="5" cy="5" r="4.2" fill="none" stroke="#fff" stroke-width="1"/><path d="M3 5.2l1.4 1.4L7.2 3.7" fill="none" stroke="#fff" stroke-width="1"/></svg>Courtesy(loaner vacuums)</li>
      <li><svg class="tick" viewBox="0 0 10 10"><circle cx="5" cy="5" r="4.2" fill="none" stroke="#fff" stroke-width="1"/><path d="M3 5.2l1.4 1.4L7.2 3.7" fill="none" stroke="#fff" stroke-width="1"/></svg>Drive Up (Curbside Service)</li>
      <li><svg class="tick" viewBox="0 0 10 10"><circle cx="5" cy="5" r="4.2" fill="none" stroke="#fff" stroke-width="1"/><path d="M3 5.2l1.4 1.4L7.2 3.7" fill="none" stroke="#fff" stroke-width="1"/></svg>(Pull in, honk, call or blink your lights and</li>
      <li class="cont">we'll carry the vacuum in for you)</li>
    </ul>

    <p class="abs round address">2270 Harbor Ave Lakeview, NY<br>10990 *Just off Route 9 Exit 4</p>
    <p class="abs condensed back-phone">555-014-2290</p>

    <div class="abs photo--tile" role="img" aria-label="Close-up photo of stone floor tiles"></div>
    <div class="abs photo--wand" role="img" aria-label="Photo of an upholstery cleaning wand in use"></div>

    <div class="abs postage">POSTAGE<br>AREA</div>
    <div class="abs mail-block">
      <p class="indicia">PRESORTED STANDARD<br>U.S. POSTAGE PAID<br>PARCELO, LLC. 10991</p>
      <p class="route">****************** ECRWSSKRTB****</p>
      <p class="recipient">Local<br>Postal Customer</p>
    </div>
    <p class="abs barcode-label">BARCODE AREA</p>
  </section>

</main>
</body>
</html>
```